An e-flyer for an exotic car and fine wine club.

This is the first meeting of Brixley Motor Society and includes several businesses. Their logos should be featured at the bottom. It should be sleek, elegant and simple featuring a photo of an Corvane Halder T7 as well as my logo (I will provide photos). The flyer needs to look professional and appeal to billionaires.
The text should read:
Brixley Motor society presents
Swift Wheels and Vintage Pours (but not while driving)
Hosted by Wrenfold Vault Rooms
Bring your best car(s) and join us to enjoy the party with sommelier selected wines, the best classic and modern cars and hors d'oeuvre catered by Dunmore's Shellfish Bar. Live DJ.
August 26th 3-6 p.m.
This event is gratis.
RSVP to nora@brixleymotorsociety.example for address and details

Target Market(s)
Very wealthy exotic car owners
Industry/Entity Type
Car Club, Fine Wines.
Requirements
Must have
- Style, panache, elegance, sleekness, simplicity. I like the idea of a black or dark flyer with a consistent color scheme.
Nice to have
- I want the flyer to be simple and sleek, feature an Corvane Halder T7 as the eye catcher, Brixley Motor Society logo featured prominently on the top, and the other business logos on the bottom.
Should not have
- It must not be too noisy or busy.

```html
<!DOCTYPE html>
<html lang="en">
<head>
<meta charset="utf-8">
<title>Swift Wheels and Vintage Pours – Brixley Motor Society</title>
<link rel="stylesheet" href="https://fonts.googleapis.com/css2?family=Montserrat:wght@400;500;700&family=Oswald:wght@300;400;700&display=swap">
<style>
  :root {
    --page: #f3f3f3;
    --ink: #131a26;
    --red: #c22f3a;
    --red-bright: #d8262f;
    --white: #ffffff;
    --soft-white: #f2f2f2;
    --navy: #0f1724;
    --photo-light: #c3c3c3;
    --photo-red: #a8343b;
    --photo-dark: #8e8e8e;
  }
  * { box-sizing: border-box; margin: 0; padding: 0; }
  html, body { width: 1200px; height: 1200px; overflow: hidden; background: var(--page); }
  .flyer {
    position: absolute; left: 209px; top: 52px; width: 782px; height: 1097px;
    background: linear-gradient(to bottom,
      #050505 0%, #5a5a5a 6%, #a7a7a7 14%, #d2d2d2 30%, #dcdcdc 45%,
      #cfcfcf 58%, #bdbdbd 70%, #9a9a9a 80%, #5e5e5e 90%, #141414 100%);
    box-shadow: 0 4px 18px rgba(0,0,0,.35);
    font-family: "Montserrat", sans-serif; color: var(--ink); text-align: center;
    overflow: hidden;
  }
  .flyer > * { position: absolute; left: 0; width: 100%; }
  .club-mark { top: 58px; display: flex; flex-direction: column; align-items: center; gap: 16px; }
  .club-mark__square { width: 46px; height: 46px; background: var(--ink); }
  .club-mark__name { font-weight: 700; font-size: 34px; letter-spacing: 3px; color: var(--ink); text-transform: uppercase; }
  .presents { top: 204px; font-size: 21px; color: #2a2a2a; }
  .title { top: 240px; font-family: "Oswald", sans-serif; font-weight: 700; font-size: 50px; color: var(--red); text-transform: uppercase; letter-spacing: .5px; }
  .subtitle { top: 306px; font-family: "Oswald", sans-serif; font-weight: 400; font-size: 38px; color: var(--ink); text-transform: uppercase; }
  .car-photo {
    top: 376px; height: 243px;
    background: linear-gradient(160deg, var(--photo-light) 0%, var(--photo-red) 50%, var(--photo-dark) 100%);
  }
  .host { top: 640px; font-size: 19px; color: var(--soft-white); display: flex; justify-content: center; align-items: center; gap: 18px; }
  .host__rule { width: 36px; height: 7px; border-top: 1.5px solid var(--ink); border-bottom: 1.5px solid var(--ink); }
  .invite { top: 664px; font-family: "Oswald", sans-serif; font-weight: 400; font-size: 30px; line-height: 44px; color: var(--red-bright); }
  .highlights { top: 704px; font-family: "Oswald", sans-serif; font-weight: 700; font-size: 36px; line-height: 42px; color: var(--navy); }
  .caterer { top: 835px; left: 50%; width: auto; transform: translateX(-50%); white-space: nowrap;
    background: var(--red-bright); color: var(--white); font-weight: 700; font-size: 16px; padding: 3px 14px; border-radius: 6px; }
  .dj { top: 864px; font-weight: 700; font-size: 28px; color: var(--white); }
  .date { top: 902px; display: flex; justify-content: center; align-items: center; gap: 12px; font-weight: 500; font-size: 21px; color: var(--white); }
  .date__arrow { width: 30px; height: 3px; background: var(--ink); clip-path: polygon(0 50%, 100% 0, 100% 100%); }
  .date__arrow--right { clip-path: polygon(0 0, 100% 50%, 0 100%); }
  .gratis { top: 936px; left: 50%; width: auto; transform: translateX(-50%); white-space: nowrap;
    background: var(--navy); color: var(--white); font-weight: 500; font-size: 17px; padding: 2px 10px; border-radius: 4px; }
  .partner { top: 993px; width: 156px; height: 78px; background: var(--white); border-radius: 8px;
    display: flex; align-items: center; justify-content: center; padding: 8px; }
  .partner--left { left: 29px; }
  .partner--right { left: 597px; }
  .partner__name { font-weight: 700; font-size: 15px; line-height: 19px; color: var(--ink); }
  .rsvp { top: 988px; left: 190px; width: 402px; color: var(--white); font-size: 14px; line-height: 22px; }
  .rsvp__email { font-weight: 700; font-size: 17px; }
</style>
</head>
<body>
  <main class="flyer">
    <header class="club-mark">
      <span class="club-mark__square"></span>
      <span class="club-mark__name">Brixley Motor Society</span>
    </header>
    <p class="presents">Presents</p>
    <h1 class="title">Swift Wheels and Vintage Pours</h1>
    <p class="subtitle">(But not while driving)</p>
    <div class="car-photo" role="img" aria-label="Photo of a red Corvane Halder T7 coupe on a race track"></div>
    <p class="host"><span class="host__rule"></span>Hosted by Wrenfold Vault Rooms<span class="host__rule"></span></p>
    <p class="invite">Bring your best car(s) and join us to enjoy the party with</p>
    <p class="highlights">sommelier selected wines,<br>the best classic and modern cars and<br>hors d'oeuvre</p>
    <p class="caterer">Catered by Dunmore's Shellfish Bar</p>
    <p class="dj">Live DJ.</p>
    <p class="date"><span class="date__arrow"></span>August 26th 3-6 p.m.<span class="date__arrow date__arrow--right"></span></p>
    <p class="gratis">This event is gratis.</p>
    <div class="partner partner--left"><span class="partner__name">Halloway Cellars</span></div>
    <p class="rsvp">RSVP to<br><span class="rsvp__email">nora@brixleymotorsociety.example</span><br>for address and details</p>
    <div class="partner partner--right"><span class="partner__name">Wrenfold Vault Rooms</span></div>
  </main>
</body>
</html>
```